Accommodation in an Executive Apartment for rent could be a Bed and breakfast,

Currently have a website and like the overall look but it needs revamping and want to add an instant booking button, which I would do later as the unit has a channel manager. Also want to be able to post blogs, etc. Need it to be viewed well on smart phones/tablets. all information related to this unit is on the current site which is www.stayfernhollowsuites.com.au if you would view websites similar to roomvista.com and tripnestly.com Must be able to be coded in Wordpress

The current design is done in Wordpress so would want this functionality in any new design.

Target Market(s)

Workers at Parliamentary triangle, Canberra. Workers at Marlowe centre Deakin, Workers at Bellbrook Ashford Hospital, Workers at Tindale Hospital, Public Servants Woden, Workers in Deakin ACT

Industry/Entity Type

Accommodation

Number of Pages Required

5+ page

Font styles to use
Sans Serif

Colors
ec1f27

Requirements
Must have
• Must have a classy look about it. Less clicks through the better. Not to wordy. Hard hitting points,
Nice to have
• Would like to retain the same colour theme and look
Should not have
• anything tacky

```html
<!DOCTYPE html>
<html lang="en">
<head>
<meta charset="utf-8">
<title>Fernhollow executive bed and breakfast</title>
<link href="https://fonts.googleapis.com/css2?family=Open+Sans:wght@400;600;700&family=Raleway:wght@400;500;600&display=swap" rel="stylesheet">
<style>
:root{
  --accent:#ec1f27;
  --accent-light:#fbd6d7;
  --ink:#2b2b2b;
  --grey:#8a8a8a;
  --charcoal:#3b3b3d;
  --night:#1d2630;
  --white:#ffffff;
}
*{margin:0;padding:0;box-sizing:border-box}
html,body{width:1200px;height:2839px;overflow:hidden}
body{position:relative;font-family:"Open Sans",Arial,sans-serif;color:var(--ink);background:var(--white)}
.abs{position:absolute}

/* header */
.site-header{left:0;top:0;width:1200px;height:80px;background:var(--white);z-index:3}
.brand{left:57px;top:19px;width:265px;height:57px;background:var(--accent);border-radius:4px 14px 4px 14px;display:flex;align-items:center;justify-content:center;color:var(--white);font-size:13.5px;font-weight:600;white-space:nowrap}
.main-nav{left:0;top:27px;width:1200px;height:20px}
.main-nav a{position:absolute;font-size:12px;color:var(--ink);text-decoration:none;text-transform:uppercase;white-space:nowrap}
.main-nav a.active{color:var(--accent)}
.nav-pointer{left:379px;top:70px;width:0;height:0;border-left:10px solid transparent;border-right:10px solid transparent;border-bottom:10px solid #3a2a20;z-index:4}

/* hero */
.hero-photo{left:0;top:80px;width:1200px;height:597px;background:linear-gradient(180deg,#c9b89a 0%,#e4d6bb 25%,#b24436 55%,#6a1d16 80%,#3a1a14 100%)}
.booking-bar{left:0;top:530px;width:1200px;height:147px;background:rgba(20,16,14,.82)}
.booking-bar .label{position:absolute;top:62px;color:var(--accent);font-size:27px;font-family:"Raleway",sans-serif;line-handle:1}
.field{position:absolute;top:68px;height:46px;border:1px solid #6a5a50;background:rgba(0,0,0,.35)}
.cal{position:absolute;left:0;top:0;width:45px;height:44px;background:var(--accent)}
.field span{position:absolute;color:var(--white);font-size:13px;top:13px}
.month{position:absolute;left:0;top:0;width:68px;height:44px;background:var(--accent);color:var(--white);font-size:12px;padding:13px 0 0 12px}
.search-btn{left:1035px;top:594px;width:116px;height:52px;background:var(--accent);color:var(--white);font-size:19px;font-weight:600;display:flex;align-items:center;justify-content:center}

/* features */
.features{left:0;top:677px;width:1200px;height:411px;background:linear-gradient(135deg,#3a2c22 0%,#24201c 50%,#3b2a1e 100%)}
.feature-line{left:172px;top:864px;width:852px;height:2px;background:rgba(255,255,255,.8)}
.feature-circle{position:absolute;top:803px;width:124px;height:124px;border-radius:50%;background:var(--accent);display:flex;align-items:center;justify-content:center}
.feature-circle.lead{background:var(--white)}
.feature{position:absolute;top:940px;width:260px;text-align:center;color:var(--white)}
.feature h3{color:var(--accent);font-size:16px;font-weight:700;letter-spacing:.5px;margin-bottom:16px}
.feature p{font-size:11.5px;line-height:16px;padding:0 10px}
.feature a{display:inline-block;margin-top:8px;color:var(--accent);font-size:11.5px;text-decoration:none}

/* welcome */
.section-title{position:absolute;left:0;width:1200px;text-align:center;font-family:"Raleway",sans-serif;font-weight:500;color:#111}
.section-title em{font-style:normal;color:var(--accent)}
.body-copy{position:absolute;left:100px;width:1000px;text-align:center;color:var(--grey);font-size:11.5px;line-height:21px}
.btn{position:absolute;background:var(--accent);color:var(--white);font-size:11px;display:flex;align-items:center;justify-content:center;text-transform:uppercase}
.btn.dark{background:var(--charcoal)}

/* newsletter */
.newsletter{left:0;top:1388px;width:1200px;height:446px;background:var(--accent)}
.newsletter h2{position:absolute;left:0;top:40px;width:1200px;text-align:center;color:var(--white);font-family:"Raleway",sans-serif;font-weight:500;font-size:36px}
.input{position:absolute;top:140px;width:388px;height:47px;background:var(--accent-light);color:#8e5a5a;font-size:11px;padding:16px 0 0 16px}
.signup{position:absolute;left:187px;top:206px;width:807px;height:49px;background:var(--charcoal);color:var(--white);font-size:20px;display:flex;align-items:center;justify-content:center}
.contact-col{position:absolute;top:290px;color:var(--ink)}
.contact-col h4{font-weight:400;font-size:19px;margin-bottom:10px}
.contact-col li{list-style:none;font-size:15px;color:var(--white);line-height:23px;display:flex;align-items:center;gap:10px}
.contact-col.left{right:628px;text-align:right}
.contact-col.left li{justify-content:flex-end}
.contact-col.right{left:636px}
.contact-divider{position:absolute;left:606px;top:292px;width:1px;height:126px;background:rgba(255,255,255,.7)}

/* services */
.service-photo{position:absolute;top:2082px;width:343px;height:197px;background:linear-gradient(135deg,#c8b08a,#8a6a48 55%,#d8c8a8)}
.service-card{position:absolute;top:2300px;width:343px}
.service-card h3{font-size:12.5px;font-weight:700;margin-bottom:10px}
.service-card h3.accent{color:var(--accent)}
.service-card p{font-size:11.5px;line-height:17px;color:#555}

/* footer */
.site-footer{left:0;top:2440px;width:1200px;height:286px;background:linear-gradient(180deg,#233041,var(--night))}
.foot-col{position:absolute;top:38px;color:var(--white)}
.foot-col h4{color:var(--accent);font-weight:400;font-size:17px;margin-bottom:14px}
.foot-col li{list-style:none;font-size:11.5px;line-height:28px;padding-left:14px;position:relative}
.foot-col li::before{content:"";position:absolute;left:0;top:12px;width:4px;height:4px;border-radius:50%;background:var(--white)}
.foot-col p{font-size:11.5px;line-height:19px;width:320px}
.foot-divider{position:absolute;top:32px;width:1px;height:220px;background:rgba(255,255,255,.25)}
.bottom-bar{left:0;top:2726px;width:1200px;height:113px;background:var(--accent);color:var(--white)}
.bottom-links{position:absolute;left:0;top:45px;width:1200px;text-align:center;font-size:11.5px}
.copyright{position:absolute;left:0;top:74px;width:1200px;text-align:center;font-size:10px}
.social{position:absolute;top:60px;width:14px;height:14px;border-radius:50%;background:rgba(255,255,255,.9)}
</style>
</head>
<body>

<header class="abs site-header">
  <div class="abs brand">Fernhollow executive bed and breakfast</div>
  <nav class="abs main-nav">
    <a class="active" style="left:371px">Home</a>
    <a style="left:450px">B&amp;B Accommodation</a>
    <a style="left:625px">Gallery</a>
    <a style="left:717px">What's Nearby</a>
    <a style="left:851px">Guest Book</a>
    <a style="left:965px">Useful Links</a>
    <a style="left:1085px">Contact Us</a>
  </nav>
</header>
<div class="abs nav-pointer"></div>

<div class="abs hero-photo" role="img" aria-label="Bedroom with red bedspread, pink cushions and two bedside lamps"></div>

<form class="abs booking-bar">
  <span class="label" style="left:47px">I am&nbsp;&nbsp;to</span>
  <div class="field" style="left:283px;width:254px">
    <svg class="abs" style="left:230px;top:19px" width="10" height="6"><path d="M0 0h10L5 6z" fill="#fff"/></svg>
  </div>
  <span class="label" style="left:566px">From</span>
  <div class="field" style="left:660px;width:134px">
    <div class="cal"><svg width="45" height="44"><rect x="16" y="15" width="14" height="14" fill="none" stroke="#fff" stroke-width="2"/><line x1="16" y1="19" x2="30" y2="19" stroke="#fff" stroke-width="2"/></svg></div>
    <span style="left:58px">Sep - 09</span>
  </div>
  <span class="label" style="left:821px">Till</span>
  <div class="field" style="left:879px;width:134px"><div class="month">Month</div></div>
</form>
<div class="abs search-btn">SEARCH</div>

<section class="abs features" role="img" aria-label="Dim photo of guests relaxing outdoors"></section>
<div class="abs feature-line"></div>
<div class="feature-circle lead" style="left:110px">
  <svg width="50" height="40"><g fill="#ec1f27"><rect x="4" y="20" width="5" height="14"/><rect x="12" y="12" width="5" height="22"/><rect x="20" y="16" width="5" height="18"/><rect x="28" y="8" width="5" height="26"/><rect x="0" y="35" width="40" height="2"/></g></svg>
</div>
<div class="feature-circle" style="left:392px">
  <svg width="60" height="60"><path d="M18 12v14a10 10 0 0 0 20 0V12M28 36v6a8 8 0 0 0 16 0v-6" fill="none" stroke="#fff" stroke-width="4"/><circle cx="44" cy="32" r="4" fill="#fff"/></svg>
</div>
<div class="feature-circle" style="left:684px">
  <svg width="50" height="50"><circle cx="25" cy="25" r="17" fill="none" stroke="#fff" stroke-width="4"/><path d="M25 15v11h-8" fill="none" stroke="#fff" stroke-width="3"/></svg>
</div>
<div class="feature-circle" style="left:962px">
  <svg width="50" height="50"><circle cx="25" cy="25" r="19" fill="#fff"/><rect x="22" y="14" width="6" height="22" fill="#ec1f27"/><rect x="14" y="22" width="22" height="6" fill="#ec1f27"/></svg>
</div>

<div class="feature" style="left:42px"><h3>CORPORATE RATES</h3><p>Weekly and monthly rates for public servants and contract workers in Deakin and Woden.</p><a>Read More ▸</a></div>
<div class="feature" style="left:324px"><h3>NEAR THE HOSPITALS</h3><p>Minutes from Bellbrook Ashford Hospital and Tindale Hospital for medical staff.</p><a>Read More ▸</a></div>
<div class="feature" style="left:616px"><h3>FLEXIBLE CHECK-IN</h3><p>Self check-in at any hour, so late shifts and early flights are never a problem.</p><a>Read More ▸</a></div>
<div class="feature" style="left:894px"><h3>INSTANT BOOKING</h3><p>Check live availability and confirm your executive apartment in a few clicks.</p><a>Read More ▸</a></div>

<section>
  <h2 class="section-title" style="top:1138px;font-size:28px">Welcome to <em>Fernhollow executive bed and breakfast</em></h2>
  <p class="body-copy" style="top:1195px">Lorem ipsum dolor sit amet, consectetur adipiscing elit, sed do eiusmod tempor incididunt ut labore et dolore magna aliqua. Ut enim ad minim veniam, quis nostrud exercitation ullamco laboris nisi ut aliquip ex ea commodo consequat. Duis aute irure dolor in reprehenderit in voluptate velit esse cillum dolore eu fugiat nulla pariatur. Excepteur sint occaecat cupidatat non proident, sunt in culpa qui officia deserunt mollit anim id est laborum.</p>
  <div class="btn" style="left:538px;top:1282px;width:121px;height:36px">Read More</div>
</section>

<section class="abs newsletter">
  <h2>Join our newsletter!</h2>
  <div class="input" style="left:187px">Enter Your Name</div>
  <div class="input" style="left:606px">Enter Your Email id</div>
  <div class="signup">SIGN UP</div>
  <div class="contact-col left">
    <h4>Need a hand?&nbsp;&nbsp; Contact Us</h4>
    <ul>
      <li>0400 555 190 <svg width="12" height="12"><path d="M2 1l3 0 1 3-2 1a7 7 0 0 0 3 3l1-2 3 1v3C6 11 1 6 2 1z" fill="#fff"/></svg></li>
      <li>info@fernhollowsuites.com.au <svg width="12" height="10"><rect width="12" height="10" fill="#fff"/><path d="M0 0l6 5 6-5" stroke="#ec1f27" fill="none"/></svg></li>
      <li>(02) 5550 1947 <svg width="12" height="12"><rect width="12" height="12" rx="2" fill="#fff"/><rect x="3" y="3" width="6" height="3" fill="#ec1f27"/></svg></li>
    </ul>
  </div>
  <div class="contact-divider"></div>
  <div class="contact-col right">
    <h4>Ready to book?&nbsp;&nbsp; Call us</h4>
    <ul>
      <li><svg width="12" height="12"><path d="M2 1l3 0 1 3-2 1a7 7 0 0 0 3 3l1-2 3 1v3C6 11 1 6 2 1z" fill="#fff"/></svg> 0400 555 271</li>
      <li><svg width="12" height="10"><rect width="12" height="10" fill="#fff"/><path d="M0 0l6 5 6-5" stroke="#ec1f27" fill="none"/></svg> info@fernhollowsuites.com.au</li>
      <li><svg width="12" height="12"><rect width="12" height="12" rx="2" fill="#fff"/><rect x="3" y="3" width="6" height="3" fill="#ec1f27"/></svg> (02) 5550 1947</li>
    </ul>
  </div>
</section>

<section>
  <h2 class="section-title" style="top:1876px;font-size:32px">Our <em>Service</em></h2>
  <p class="body-copy" style="top:1940px">Lorem ipsum dolor sit amet, consectetur adipiscing elit, sed do eiusmod tempor incididunt ut labore et dolore magna aliqua. Ut enim ad minim veniam, quis nostrud exercitation ullamco laboris. Duis aute irure dolor in reprehenderit in voluptate velit esse cillum dolore eu fugiat nulla pariatur.</p>
  <p class="body-copy" style="top:2001px">Duis aute irure dolor in reprehenderit in voluptate velit esse cillum dolore eu fugiat nulla pariatur. Excepteur sint occaecat cupidatat non proident, sunt in culpa qui officia deserunt mollit anim id est laborum.</p>

  <div class="service-photo" style="left:47px" role="img" aria-label="Lounge room with armchairs and red cushions"></div>
  <div class="service-photo" style="left:430px" role="img" aria-label="Open-plan living and kitchen area"></div>
  <div class="service-photo" style="left:812px;background:linear-gradient(135deg,#f0e6c8,#c89a5a 55%,#e8dcc0)" role="img" aria-label="Kitchen with timber benchtop"></div>

  <div class="service-card" style="left:47px"><h3 class="accent">EXECUTIVE LIVING ROOM</h3><p>Lorem ipsum dolor sit amet, consectetur adipiscing elit, sed do eiusmod tempor incididunt</p></div>
  <div class="service-card" style="left:430px"><h3>OPEN-PLAN APARTMENT</h3><p>Lorem ipsum dolor sit amet, consectetur adipiscing elit, sed do eiusmod tempor incididunt</p></div>
  <div class="service-card" style="left:812px"><h3>FULLY EQUIPPED KITCHEN</h3><p>Lorem ipsum dolor sit amet, consectetur adipiscing elit, sed do eiusmod tempor incididunt</p></div>
  <div class="btn" style="left:47px;top:2372px;width:97px;height:33px">Read More</div>
  <div class="btn dark" style="left:430px;top:2372px;width:97px;height:33px">Read More</div>
  <div class="btn dark" style="left:812px;top:2372px;width:97px;height:33px">Read More</div>
</section>

<footer class="abs site-footer" role="img" aria-label="Faint silhouettes of city landmarks on a dark sky">
  <div class="foot-col" style="left:49px">
    <h4>About Us</h4>
    <p>Lorem ipsum dolor sit amet, consectetur adipiscing elit, sed do eiusmod tempor incididunt ut labore et dolore magna aliqua. Ut enim ad minim veniam, quis nostrud exercitation ullamco laboris tempor incididunt ut labore et dolore magna aliqua. Ut enim ad minim veniam, quis nostrud exercitation ullamco laboris</p>
  </div>
  <div class="btn" style="left:52px;top:203px;width:104px;height:30px;text-transform:none">Read More</div>
  <div class="foot-divider" style="left:405px"></div>
  <div class="foot-col" style="left:435px">
    <h4>Your Stay</h4>
    <ul><li>Executive Apartment</li><li>Bed and Breakfast</li><li>Weekly Corporate Rates</li><li>Long-term Stays</li><li>Secure Parking</li><li>Fast Wi-Fi</li></ul>
  </div>
  <div class="foot-divider" style="left:695px"></div>
  <div class="foot-col" style="left:729px">
    <h4>Support</h4>
    <ul><li>Change a Booking</li><li>Ask a Question</li><li>Frequently Asked Question</li><li>Booking Terms</li><li>Contacts</li></ul>
  </div>
  <div class="foot-divider" style="left:975px"></div>
  <div class="foot-col" style="left:1003px">
    <h4>About</h4>
    <ul><li>Contacts</li><li>Blog</li><li>Privacy Policy</li><li>House Rules</li><li>What's Nearby</li></ul>
  </div>
</footer>

<div class="abs bottom-bar">
  <div class="bottom-links">Home&nbsp; / &nbsp;About Us&nbsp; / &nbsp;Our Services&nbsp; / &nbsp;Testimonials&nbsp; / &nbsp;Gallery&nbsp; / &nbsp;Contact</div>
  <div class="copyright">© All Rights Reserved. Copyrights @Fernhollow executive bed and breakfast</div>
  <span class="social" style="left:978px"></span>
  <span class="social" style="left:1018px"></span>
  <span class="social" style="left:1056px"></span>
  <span class="social" style="left:1094px"></span>
  <span class="social" style="left:1132px"></span>
</div>

</body>
</html>
```